DIGITAL MENUS

Hi Odette (This project is for Odette ONLY)Hope you are well. Can you please help me with designing a new menu for me.I've attached my current menu for you. I would like a new layout using photos for each items.You can use same photos as the menu board that you have designed for me before.Layout must be in Landscape form as current menu. JPEG files.

• Hi Odette,
• Ideal layout:
• DISPLAY MENU #1:
• Rice paper Rolls and Spring rolls
• Pho
• DISPLAY MENU #2:
• Noodle Salads
• Rice
• Stirfry Noodles
• DISPLAY MENU #3:
• Drinks
• 1. All soft drinks $3
• 2. Brae Hollin water $3
• 3. T. Varzoni Sparkling water $4.5
• 4. Qualo Water $4.5
• 5. Brindel Ice-Tea $4.5
• 6. Orvane Juices $5
• 7. Kombucha $5
• and Vietnamese Drinks

```html
<!DOCTYPE html>
<html lang="en">
<head>
<meta charset="utf-8">
<title>Drinks Menu</title>
<link href="https://fonts.googleapis.com/css2?family=Libre+Baskerville:ital,wght@0,700;1,400&family=Ultra&display=swap" rel="stylesheet">
<style>
  :root {
    --board-dark: #170b0c;
    --board-red: #2a1012;
    --ink-light: #ffffff;
    --divider: #ffffff;
    --photo-dark: #0d0d0e;
    --photo-green: #b9c98e;
    --photo-yellow: #f3d98f;
  }
  html, body {
    margin: 0;
    padding: 0;
    overflow: hidden;
    background: var(--board-dark);
  }
  .menu-board {
    position: relative;
    width: 1200px;
    height: 673px;
    overflow: hidden;
    background: linear-gradient(135deg, var(--board-red), var(--board-dark) 60%);
  }
  .feature-art {
    position: absolute;
    inset: 0;
    width: 1200px;
    height: 673px;
  }
  .menu-title {
    position: absolute;
    left: 720px;
    width: 420px;
    top: 14px;
    margin: 0;
    text-align: center;
    font-family: "Ultra", serif;
    font-weight: 400;
    font-size: 76px;
    line-height: 1;
    letter-spacing: 3px;
    color: var(--ink-light);
    text-shadow: 3px 3px 0 var(--board-dark), 5px 5px 0 var(--ink-light);
  }
  .title-rule {
    position: absolute;
    left: 720px;
    top: 94px;
    width: 419px;
    border-top: 4px dotted var(--ink-light);
  }
  .drink-list {
    position: absolute;
    left: 622px;
    top: 136px;
    width: 564px;
    margin: 0;
    padding: 0;
    list-style: none;
  }
  .drink-item {
    display: flex;
    justify-content: space-between;
    align-items: baseline;
    height: 57.7px;
    color: var(--ink-light);
  }
  .drink-name {
    font-family: "Libre Baskerville", serif;
    font-style: italic;
    font-size: 30px;
    letter-spacing: -0.5px;
  }
  .drink-price {
    font-family: "Libre Baskerville", serif;
    font-weight: 700;
    font-size: 32px;
  }
</style>
</head>
<body>
  <main class="menu-board">
    <svg class="feature-art" viewBox="0 0 1200 673" aria-hidden="false">
      <defs>
        <linearGradient id="photoTone" x1="0" y1="0" x2="1" y2="0">
          <stop offset="0" stop-color="var(--photo-green)"/>
          <stop offset="0.55" stop-color="var(--photo-green)"/>
          <stop offset="0.7" stop-color="var(--photo-yellow)"/>
          <stop offset="1" stop-color="var(--photo-dark)"/>
        </linearGradient>
      </defs>
      <polygon role="img" aria-label="Photo of a green smoothie and a mango smoothie in clear cups on a dark table"
        points="0,0 645,0 496,673 0,673" fill="url(#photoTone)"/>
      <polygon class="photo-divider" points="645,0 651,0 502,673 496,673" fill="var(--divider)"/>
    </svg>

    <h1 class="menu-title">Drinks</h1>
    <div class="title-rule"></div>

    <ul class="drink-list">
      <li class="drink-item"><span class="drink-name">All soft drinks</span><span class="drink-price">$3.00</span></li>
      <li class="drink-item"><span class="drink-name">Brae Hollin water</span><span class="drink-price">$3.00</span></li>
      <li class="drink-item"><span class="drink-name">T. Varzoni Sparkling water</span><span class="drink-price">$4.50</span></li>
      <li class="drink-item"><span class="drink-name">Qualo Water</span><span class="drink-price">$4.50</span></li>
      <li class="drink-item"><span class="drink-name">Brindel Ice-Tea</span><span class="drink-price">$4.50</span></li>
      <li class="drink-item"><span class="drink-name">Orvane Juices</span><span class="drink-price">$5.00</span></li>
      <li class="drink-item"><span class="drink-name">Kombucha</span><span class="drink-price">$5.00</span></li>
      <li class="drink-item"><span class="drink-name">Vietnamese Drinks</span><span class="drink-price">$5.00</span></li>
    </ul>
  </main>
</body>
</html>
```